Brontal Land Associates Web Site

We need a website design for a new land purchasing and development business based in PEI. We are just regular guys trying a new adventure buying small parcels of land, doing the hard work seperating them into lots, building roads and selling off a dream location. We help folks like ourselves buy the lots, create a house plan and help get the project done.

We have a wordpress website, but no skills. The site should have our simple story and links to individual land development progects, currently we have 2. The larger project is on a golf course and images have been uploaded. We would like a map of the properities with locations on the properties you can click to see the views/ pictures. It would be great to have the ability to superimpose house images on the lot images. This would help prospects see the end results. I have attached some photos and logo's, however, they are not manditory.
The project would have to allow for us to update and maintain the site.

Target Market(s)

Visitors to PEI, typically from larger cities in Ontario and Maine. Golfers that want to live on a golf course.

Industry/Entity Type

Realestate (land development)

Coding

Coded - Design and coding required

Number of Pages Required

4 page

Requirements
Must have
• Allow fo us to maintain the site. Company overview page with story and contact information. Links to current realestate projects (developments). Project pages with the informaiton on the land and purchasing. Since this is land not houses, maps to the site, maps of the parcel, maps of the individual lots with the ability to review photos based on the views of that particular lot.
Nice to have
• The ability to upload and overlay a house picture on the lot. This would provide a visual of the final build.

```html
<!DOCTYPE html>
<html lang="en">
<head>
<meta charset="utf-8">
<title>Brontal Land Associates</title>
<link href="https://fonts.googleapis.com/css2?family=Playfair+Display:wght@400;500&family=Poppins:wght@400;500;600&display=swap" rel="stylesheet">
<style>
:root{
  --green:#7fb26d;
  --green-soft:#92bd7f;
  --green-pale:#e6f0e0;
  --ink:#222222;
  --text:#444444;
  --white:#ffffff;
  --footer:#2b2b2b;
  --footer-line:#444444;
  --serif:'Playfair Display', Georgia, serif;
  --sans:'Poppins', Arial, sans-serif;
}
*{box-sizing:border-box;margin:0;padding:0}
html,body{width:1200px;height:3649px;overflow:hidden;background:var(--white)}
h1,h2,h3,h4{font-weight:400}
.page{position:relative;width:1200px;height:3649px;overflow:hidden;font-family:var(--sans);color:var(--text)}
.abs{position:absolute}

/* header */
.brand{display:flex;align-items:center;gap:10px}
.brand-dot{width:64px;height:64px;border-radius:50%;background:var(--green)}
.brand-name{font-family:var(--serif);font-size:27px;color:var(--ink);letter-spacing:.5px}
.nav{top:31px;left:712px;display:flex;gap:38px;font-size:15px;color:var(--ink)}
.nav a{color:inherit;text-decoration:none;display:flex;align-items:center;gap:8px}
.nav a.active{color:var(--green)}

/* hero */
.hero{top:0;left:0;width:1200px;height:793px;
  background:linear-gradient(180deg,#eaf5fb 0%,#f4f7ee 30%,#dfe9d6 42%,#5d6b44 50%,#8a9650 60%,#b49a5e 78%,#c39a6a 100%)}
.hero-title{top:214px;left:0;width:1200px;text-align:center;font-family:var(--serif);font-size:56px;line-height:62px;color:var(--ink)}
.btn{display:flex;align-items:center;justify-content:center;border-radius:26px;font-size:15px;font-weight:600;letter-spacing:1px;text-transform:uppercase;text-decoration:none}
.btn-green{top:414px;left:513px;width:174px;height:48px;background:var(--green);color:var(--white)}

/* about */
.photo-about{top:881px;left:89px;width:567px;height:489px;background:linear-gradient(180deg,#fbf2b8 0%,#e8d98a 25%,#8fa94a 45%,#6f9a31 70%,#53801f 100%)}
.about-kicker{top:972px;left:623px;font-family:var(--serif);font-size:48px;line-height:60px;color:var(--ink)}
.about-title{top:1025px;left:623px;font-family:var(--serif);font-size:68px;line-height:80px;color:var(--ink);letter-spacing:1px}
.about-text{top:1118px;left:690px;width:425px;font-size:14.5px;line-height:25.7px;color:var(--text)}

.section-title{top:1470px;left:0;width:1200px;text-align:center;font-family:var(--serif);font-size:65px;line-height:80px;color:var(--ink)}

/* projects */
.photo-ridge{top:1594px;left:521px;width:679px;height:526px;background:linear-gradient(180deg,#eef1e6 0%,#3f5a2c 12%,#5a7a34 40%,#7aaa35 60%,#5e9a27 100%)}
.project-name{font-family:var(--serif);font-size:50px;line-height:64px;color:var(--ink)}
.project-text{width:385px;font-size:14.5px;line-height:25.8px;color:var(--text)}
.arrow-btn{width:58px;height:52px}
.photo-sands{top:2199px;left:86px;width:1025px;height:524px;background:linear-gradient(160deg,#a9c98a 0%,#7fae5a 35%,#5f8f3b 65%,#3f6b2b 100%)}
.card{top:2373px;left:584px;width:460px;height:417px;background:var(--white);box-shadow:0 24px 40px rgba(0,0,0,.08)}

/* cta */
.cta{top:2885px;left:0;width:1200px;height:341px;background:var(--green-soft);border-bottom:2px solid #6ea859}
.cta-title{top:2978px;left:0;width:1200px;text-align:center;font-family:var(--serif);font-size:39px;line-height:46px;color:var(--white)}
.btn-white{top:3085px;left:513px;width:174px;height:48px;background:var(--white);color:var(--ink)}

/* footer */
.footer{top:3228px;left:0;width:1200px;height:421px;background:var(--footer)}
.footer-brand .brand-dot{width:74px;height:74px}
.footer-brand .brand-name{color:var(--white);font-size:34px}
.col-title{font-size:22px;font-weight:500;color:var(--white);text-transform:uppercase}
.col-links{list-style:none;font-size:15px;line-height:27px;color:#e6e6e6}
.newsletter-sub{font-size:15px;color:#e6e6e6}
.email{top:3416px;left:852px;width:259px;height:46px;border-radius:23px;background:#3a3a3a;display:flex;align-items:center;justify-content:space-between;padding:0 22px;font-size:13px;color:#cfcfcf}
.divider{top:3586px;left:88px;width:1023px;height:1px;background:var(--footer-line)}
.copyright{top:3607px;left:94px;font-size:13px;font-weight:500;color:var(--white)}
.socials{top:3611px;left:998px;display:flex;gap:18px}
.socials span{width:13px;height:13px;border-radius:50%;background:var(--white)}
.to-top{top:3566px;left:1135px;width:40px;height:40px;border-radius:50%;background:var(--green);display:flex;align-items:center;justify-content:center}
</style>
</head>
<body>
<div class="page">

  <section class="hero abs" role="img" aria-label="Houses overlooking rolling golf course fields at sunset"></section>

  <header>
    <div class="brand abs" style="top:10px;left:88px">
      <span class="brand-dot"></span>
      <span class="brand-name">BRONTAL</span>
    </div>
    <nav class="nav abs">
      <a class="active" href="#"><svg width="15" height="13" viewBox="0 0 15 13"><path d="M7.5 0 15 6.5h-2V13H9V9H6v4H2V6.5H0z" fill="#7fb26d"/></svg>Home</a>
      <a href="#">About</a>
      <a href="#">Projects</a>
      <a href="#">Contact Us</a>
    </nav>
  </header>

  <h1 class="hero-title abs">Discover a life away<br>from the hustle and bustle<br>of the city!</h1>
  <a class="btn btn-green abs" href="#">Contact Us</a>

  <div class="photo-about abs" role="img" aria-label="Golf course green with sand bunkers in warm morning light"></div>
  <h2 class="about-kicker abs">About</h2>
  <h2 class="about-title abs">BRONTAL</h2>
  <p class="about-text abs">We are a small development team looking for projects that are close to our hearts and represent locations and services we want available to us.&nbsp; We are experienced project managers and builders who will help our buyers find the right location, right builders and right managers for their property.</p>

  <h2 class="section-title abs">Our Projects</h2>

  <h3 class="project-name abs" style="top:1718px;left:87px">Cedar Bluff</h3>
  <p class="project-text abs" style="top:1795px;left:89px">Lorem Ipsum is simply dummy text of the printing and typesetting industry. Lorem Ipsum has been the industry's standard dummy text ever since the 1500s, when an unknown printer took a galley of type and scrambled it to make a type speci-men book. It has survived not only.</p>
  <svg class="arrow-btn abs" style="top:1972px;left:89px" viewBox="0 0 58 52"><circle cx="32" cy="26" r="26" fill="#e6f0e0"/><path d="M2 26h30M22 16l10 10-10 10" stroke="#7fb26d" stroke-width="2.5" fill="none"/></svg>
  <div class="photo-ridge abs" role="img" aria-label="Golfers on a green tee with forest behind"></div>

  <div class="photo-sands abs" role="img" aria-label="Aerial view of golf course fairways with homes and trees"></div>
  <div class="card abs"></div>
  <h3 class="project-name abs" style="top:2439px;left:628px">Harbour Greens</h3>
  <p class="project-text abs" style="top:2510px;left:634px">Lorem Ipsum is simply dummy text of the printing and typesetting industry. Lorem Ipsum has been the industry's standard dummy text ever since the 1500s, when an unknown printer took a galley of type and scrambled it to make a type speci-men book. It has survived not only.</p>
  <svg class="arrow-btn abs" style="top:2680px;left:634px" viewBox="0 0 58 52"><circle cx="32" cy="26" r="26" fill="#e6f0e0"/><path d="M2 26h30M22 16l10 10-10 10" stroke="#7fb26d" stroke-width="2.5" fill="none"/></svg>

  <section class="cta abs" role="img" aria-label="Faint farmhouse scene behind green overlay"></section>
  <h2 class="cta-title abs">Looking to invest in a property and<br>build a second home or retirement home?</h2>
  <a class="btn btn-white abs" href="#">Contact Us</a>

  <footer class="footer abs"></footer>
  <div class="brand footer-brand abs" style="top:3368px;left:88px">
    <span class="brand-dot"></span>
    <span class="brand-name">BRONTAL</span>
  </div>

  <h4 class="col-title abs" style="top:3338px;left:414px">Useful Links</h4>
  <ul class="col-links abs" style="top:3378px;left:415px"><li>Home</li><li>About</li><li>Projects</li><li>Contact Us</li></ul>

  <h4 class="col-title abs" style="top:3338px;left:643px">Projects</h4>
  <ul class="col-links abs" style="top:3378px;left:643px"><li>Cedar Bluff</li><li>Harbour Greens</li></ul>

  <h4 class="col-title abs" style="top:3338px;left:856px">Newsletter</h4>
  <p class="newsletter-sub abs" style="top:3380px;left:857px">Subscribe to our newsletter</p>
  <div class="email abs"><span>Email Address</span><svg width="14" height="14" viewBox="0 0 14 14"><path d="M14 0 0 6l5 2 1 6 2-4 4 3z" fill="#7fb26d"/></svg></div>

  <div class="divider abs"></div>
  <p class="copyright abs">© Copyright 2023 All Rights Reserved</p>
  <div class="socials abs"><span></span><span></span><span></span><span></span></div>
  <div class="to-top abs"><svg width="10" height="7" viewBox="0 0 10 7"><path d="M1 6l4-4 4 4" stroke="#fff" stroke-width="1.6" fill="none"/></svg></div>

</div>
</body>
</html>
```